New Business Card Design Project

I have a logo I would like to use on the business card. I want something that will stand out and that will be remembered.

Target Market(s)

People who collect gems, minerals and crystals.

Contact Information for Business Card

email - tkstonefalcon@mailbrook.net
phone # 617-203-4958

Font styles to use
Serif
Sans Serif
Decorative

Colors

Designer to choose colors to be used in the design.

Requirements
Must have
• The logo...two to choose from.
Nice to have
• An eye catching and memorable way to draw in people who collect gems minerals and crystals.

```html
<!DOCTYPE html>
<html lang="en">
<head>
<meta charset="utf-8">
<title>The Stone Falcon – Business Card</title>
<link rel="stylesheet" href="https://fonts.googleapis.com/css2?family=Graduate&family=Open+Sans:wght@400;600&family=Saira+Semi+Condensed:wght@700&display=swap">
<style>
  :root {
    --bg: #3a3a3a;
    --card: #1f1f20;
    --card-edge: #2a2a2b;
    --white: #eeeeee;
    --grey: #cfcfcf;
    --blue: #1a2fd0;
    --art-light: #5a5a5c;
    --art-dark: #242425;
  }
  * { margin: 0; padding: 0; box-sizing: border-box; }
  html, body { width: 799px; height: 1200px; overflow: hidden; }
  body {
    background: var(--bg);
    position: relative;
    font-family: "Open Sans", sans-serif;
  }
  .card {
    position: absolute;
    left: 80px;
    width: 640px;
    height: 366px;
    background: var(--card);
    border: 1px solid var(--card-edge);
    border-radius: 4px;
    overflow: hidden;
  }
  .card--front { top: 110px; }
  .card--back { top: 720px; }

  .wordmark {
    font-family: "Graduate", serif;
    color: var(--white);
    line-height: 1;
    letter-spacing: 1px;
  }
  .wordmark-dot {
    display: inline-block;
    width: 22px; height: 22px;
    border-radius: 50%;
    background: var(--blue);
    vertical-align: middle;
    margin-right: 12px;
  }
  .rule {
    height: 2px;
    background: var(--blue);
  }
  .tagline {
    font-family: "Saira Semi Condensed", sans-serif;
    font-weight: 700;
    letter-spacing: 3px;
  }

  /* Front */
  .front-brand {
    position: absolute;
    left: 0; right: 0; top: 128px;
    text-align: center;
  }
  .front-brand .wordmark { font-size: 40px; }
  .front-brand .rule { width: 380px; margin: 16px auto 10px; }
  .front-brand .tagline { color: var(--blue); font-size: 17px; }

  /* Back */
  .back-art {
    position: absolute;
    left: 0; top: 20px;
    width: 300px; height: 346px;
    background: radial-gradient(ellipse at 45% 40%, var(--art-light), var(--art-dark) 75%);
    border-radius: 40% 40% 0 0;
  }
  .back-info {
    position: absolute;
    right: 34px; top: 48px;
    width: 300px;
    text-align: right;
  }
  .back-info .wordmark { font-size: 30px; }
  .back-info .rule { margin: 10px 0 26px; }
  .person-name { color: var(--white); font-size: 22px; font-weight: 600; }
  .person-role { color: var(--grey); font-size: 13px; margin-bottom: 18px; }
  .contact-line {
    color: var(--grey);
    font-size: 15px;
    display: flex; justify-content: flex-end; align-items: center; gap: 8px;
    margin-top: 4px;
  }
  .contact-line svg { width: 14px; height: 14px; fill: var(--blue); }
  .back-tagline {
    position: absolute;
    right: 34px; bottom: 26px;
    color: var(--white);
    font-size: 19px;
  }
</style>
</head>
<body>
  <section class="card card--front">
    <div class="front-brand">
      <div class="wordmark"><span class="wordmark-dot"></span>THE STONE FALCON</div>
      <div class="rule"></div>
      <div class="tagline">GEMS · MINERALS · CRYSTALS</div>
    </div>
  </section>

  <section class="card card--back">
    <div class="back-art" role="img" aria-label="Large embossed mascot illustration holding a crystal cluster"></div>
    <div class="back-info">
      <div class="wordmark">THE STONE FALCON</div>
      <div class="rule"></div>
      <div class="person-name">Tara Kell Simms</div>
      <div class="person-role">Managing Director</div>
      <div class="contact-line">617-203-4958
        <svg viewBox="0 0 24 24" aria-hidden="true"><path d="M6.6 10.8a15 15 0 006.6 6.6l2.2-2.2a1 1 0 011-.25 11.4 11.4 0 003.6.57 1 1 0 011 1V20a1 1 0 01-1 1A17 17 0 013 4a1 1 0 011-1h3.5a1 1 0 011 1c0 1.25.2 2.45.57 3.6a1 1 0 01-.25 1z"/></svg>
      </div>
      <div class="contact-line">tkstonefalcon@mailbrook.net
        <svg viewBox="0 0 24 24" aria-hidden="true"><path d="M2 5h20v14H2z M2 5l10 8 10-8" fill="none" stroke="#1a2fd0" stroke-width="2"/></svg>
      </div>
    </div>
    <div class="back-tagline tagline">GEMS · MINERALS · CRYSTALS</div>
  </section>
</body>
</html>
```